TALL WAVE

I am in this industry for last 15 years we have done lots of commercial site like we work with ORBEL costruction, loam properties, DRV, quill construction.
We do all domestic and commercial wall and floor tiling, swimming pools, spas, paving, marbles blue stones and muchmore.

Specializing in the wall and floor Tiling, Waterproofing and floor preparations

Industry/Entity Type

Industry

Number of Pages Required

1 page

Font styles to use
Serif
Decorative

Colors

Designer to choose colors to be used in the design.

Requirements
Must have
• domestic and commercial indoor tiling, bathroom tiling and paving pictures
Nice to have
• beautiful bathroom pictures with tile

```html
<!DOCTYPE html>
<html lang="en">
<head>
<meta charset="utf-8">
<title>Tall Wave – Wall &amp; Floor Tiling</title>
<link href="https://fonts.googleapis.com/css2?family=Roboto+Condensed:wght@400;700&family=Open+Sans:wght@400;600;700&display=swap" rel="stylesheet">
<style>
:root{
  --green:#8dc63f;
  --green-dark:#76ab2c;
  --ink:#2b2b2b;
  --text:#6b6b6b;
  --light:#f0f0f0;
  --footer:#2a2a2a;
  --footer-bar:#1e1e1e;
  --white:#ffffff;
}
*{box-sizing:border-box;margin:0;padding:0}
html,body{width:1200px;height:3124px;overflow:hidden}
body{font-family:"Open Sans",sans-serif;color:var(--text);background:var(--white);font-size:13px;line-height:1.7}
h1,h2,h3,h4,.logo,.nav a,.btn{font-family:"Roboto Condensed",sans-serif}
.btn{display:inline-block;background:var(--green);color:var(--white);font-size:12px;font-weight:700;text-transform:uppercase;padding:7px 18px;letter-spacing:.5px}
.btn-outline{display:inline-block;border:1px solid #bbb;color:#777;font-size:10px;padding:2px 12px}

/* hero */
.hero{position:relative;height:608px;background:linear-gradient(180deg,#6c6a66 0%,#a19d97 45%,#c9c5bf 70%,#8f8b85 100%)}
.hero-photo{position:absolute;inset:0}
.topbar{position:absolute;top:0;left:0;right:0;height:64px;background:rgba(20,20,20,.7);display:flex;align-items:center;justify-content:space-between;padding:0 100px}
.logo{font-size:34px;font-weight:700;color:var(--white);letter-spacing:.5px}
.nav{display:flex;gap:6px}
.nav a{color:var(--white);font-size:14px;font-weight:700;text-decoration:none;padding:6px 12px}
.nav a.active{color:var(--green)}
.hero-copy{position:absolute;top:284px;left:0;right:0;text-align:center;color:var(--white)}
.hero-copy h1{font-size:52px;line-height:1.05;font-weight:700;text-transform:uppercase;text-shadow:0 2px 8px rgba(0,0,0,.35)}
.hero-copy .btn{margin-top:26px}
.arrow{position:absolute;top:320px;width:30px;height:30px;border-radius:50%;background:rgba(0,0,0,.45)}
.arrow.left{left:24px}.arrow.right{right:24px}

/* welcome */
.welcome{height:412px;display:flex;gap:60px;padding:112px 100px 0}
.video{width:340px;height:220px;background:linear-gradient(135deg,#d8d3cb,#a89d8c 60%,#7c6f5e);position:relative;flex:none}
.play{position:absolute;left:50%;top:50%;width:52px;height:36px;margin:-18px 0 0 -26px;background:rgba(0,0,0,.75);border-radius:8px}
.welcome-copy{padding-top:20px}
.welcome-copy h2{font-size:38px;color:var(--ink);font-weight:700;text-transform:uppercase;line-height:1.1;margin-bottom:18px}
.welcome-copy h2 span{color:var(--green)}
.welcome-copy p{font-size:12px;margin-bottom:12px;max-width:540px}
.welcome-copy .btn{margin-top:6px}

/* services */
.services{height:580px;background:var(--light);padding-top:148px;text-align:center}
.section-title{font-size:34px;color:var(--ink);font-weight:700;text-transform:uppercase}
.services-grid{display:flex;justify-content:center;gap:40px;margin-top:56px}
.service{width:210px}
.service svg{height:86px;width:100px}
.service h3{font-size:17px;color:var(--ink);font-weight:700;text-transform:uppercase;margin:14px 0 8px}
.service p{font-size:11px;line-height:1.6;margin-bottom:12px}

/* work */
.work{height:720px;padding-top:84px;text-align:center}
.gallery{display:grid;grid-template-columns:312px 388px 272px;grid-template-rows:216px 228px;gap:12px 16px;margin:60px 100px 0;width:1000px}
.tile{position:relative}
.tile-1{background:linear-gradient(160deg,#e4e2dd,#9f9a92 55%,#5e5249)}
.tile-2{background:var(--green);display:flex;flex-direction:column;align-items:center;justify-content:center;color:var(--white)}
.tile-2 h4{font-size:18px;font-weight:700;text-transform:uppercase;line-height:1.2;width:250px}
.tile-2 .plus{font-size:38px;line-height:1;margin-top:12px}
.tile-3{background:linear-gradient(160deg,#c8d0c4,#6f7c5a 50%,#3f4739)}
.tile-4{background:linear-gradient(160deg,#e8ecef,#a6b4bf 55%,#5d6d7a)}
.tile-5{background:linear-gradient(160deg,#c58155,#9c5d3a 55%,#e4ded6)}
.tile-6{background:linear-gradient(160deg,#8ea86a,#6b8a4a 45%,#8c8984)}

/* testimonials */
.testimonials{height:400px;background:linear-gradient(135deg,var(--green) 0%,var(--green-dark) 100%);padding-top:70px;text-align:center;color:var(--white)}
.testimonials .section-title{color:var(--white)}
.quotes{display:flex;gap:80px;justify-content:center;margin-top:60px;text-align:left}
.quote{display:flex;gap:24px;width:470px;position:relative}
.avatar{width:110px;height:110px;border-radius:50%;background:#e9eef0;border:5px solid var(--white);flex:none}
.quote p{font-size:12px;font-style:italic;line-height:1.6}
.quote .who{font-size:12px;margin-top:8px}
.stars{letter-spacing:2px;font-size:12px}
.qmark{position:absolute;right:0;bottom:-14px;font-family:"Roboto Condensed",sans-serif;font-size:64px;font-weight:700;line-height:1}

/* footer */
.footer{height:360px;background:var(--footer);padding:58px 100px 0;display:flex;gap:0;color:#bbb}
.footer h4{font-size:18px;color:var(--white);font-weight:700;text-transform:uppercase;margin-bottom:16px}
.col-links{width:210px}
.col-links li{list-style:none;font-size:11px;line-height:1.9;padding-left:14px;position:relative}
.col-links li::before{content:"";position:absolute;left:0;top:9px;width:4px;height:4px;background:var(--green)}
.col-contact{width:320px}
.col-contact .row{display:flex;gap:12px;font-size:11px;margin-bottom:12px;align-items:flex-start}
.col-contact svg{flex:none;margin-top:2px}
.social{display:flex;gap:8px;margin-top:6px}
.social span{width:20px;height:20px;border-radius:50%;border:1px solid #888}
.col-quote{flex:1}
.col-quote p{font-size:11px;margin-bottom:12px}
.form{display:grid;grid-template-columns:1fr 1fr;gap:8px}
.field{height:30px;border:1px solid #555;background:#333;font-size:11px;color:#999;padding:6px 10px}
.form .btn{text-align:center;padding:8px}
.copyright{height:44px;background:var(--footer-bar);color:#888;font-size:11px;text-align:center;line-height:44px}
</style>
</head>
<body>

<header class="hero">
  <div class="hero-photo" role="img" aria-label="Photo of a bright tiled bathroom with a freestanding bath, vanity and orchids"></div>
  <div class="topbar">
    <div class="logo">TALL WAVE</div>
    <nav class="nav">
      <a class="active">HOME</a><a>ABOUT US</a><a>OUR SERVICES</a><a>GALLERY</a><a>BLOG</a><a>CONTACT US</a>
    </nav>
  </div>
  <span class="arrow left"></span><span class="arrow right"></span>
  <div class="hero-copy">
    <h1>Tall Wave<br>Bathroom Tiling</h1>
    <a class="btn">Read More</a>
  </div>
</header>

<section class="welcome">
  <div class="video" role="img" aria-label="Video still of a modern tiled bathroom interior">
    <span class="play"></span>
  </div>
  <div class="welcome-copy">
    <h2>Welcome to <span>Tall Wave</span></h2>
    <p>For over fifteen years we have tiled homes and commercial sites across the region, from small ensuites to large lobbies. Every job is planned with care, set out by hand and finished to a clean, lasting line.</p>
    <p>We handle wall and floor tiling, swimming pools, spas, paving, marble and bluestone, with waterproofing and floor preparation done in house so each surface is ready for years of use.</p>
    <a class="btn">Read More</a>
  </div>
</section>

<section class="services">
  <h2 class="section-title">Our Services</h2>
  <div class="services-grid">
    <div class="service">
      <svg viewBox="0 0 100 86" fill="none" stroke="var(--green)" stroke-width="4">
        <path d="M20 10 L80 4 L80 76 L20 82 Z" fill="var(--green)" fill-opacity=".25"/>
        <path d="M20 28 L80 22 M20 46 L80 40 M20 64 L80 58 M50 7 L50 25 M35 27 L35 45 M65 24 L65 42 M50 43 L50 61 M35 63 L35 81 M65 60 L65 78"/>
      </svg>
      <h3>Wall Tiling</h3>
      <p>Neat, level wall tiling for kitchens, bathrooms and feature walls.</p>
      <span class="btn-outline">Learn More</span>
    </div>
    <div class="service">
      <svg viewBox="0 0 100 86" fill="none" stroke="var(--green)" stroke-width="4">
        <rect x="14" y="6" width="72" height="72"/>
        <path d="M14 30 L38 6 M14 54 L62 6 M14 78 L86 6 M38 78 L86 30 M62 78 L86 54"/>
      </svg>
      <h3>Floor Tiling</h3>
      <p>Durable floor tiling in porcelain, stone and marble for any room.</p>
      <span class="btn-outline">Learn More</span>
    </div>
    <div class="service">
      <svg viewBox="0 0 100 86" fill="var(--green)">
        <path d="M50 4 C50 4 30 30 30 42 a20 20 0 0 0 40 0 C70 30 50 4 50 4Z"/>
        <path d="M22 34 C22 34 12 48 12 54 a10 10 0 0 0 20 0 C32 48 22 34 22 34Z"/>
        <path d="M78 34 C78 34 68 48 68 54 a10 10 0 0 0 20 0 C88 48 78 34 78 34Z"/>
        <rect x="8" y="74" width="84" height="8"/>
      </svg>
      <h3>Waterproofing</h3>
      <p>Sealed membranes that keep wet areas dry and protect the structure.</p>
      <span class="btn-outline">Learn More</span>
    </div>
    <div class="service">
      <svg viewBox="0 0 100 86" fill="none" stroke="var(--green)" stroke-width="4">
        <path d="M12 30 L88 30 L88 80 L12 80 Z" fill="var(--green)" fill-opacity=".25"/>
        <path d="M12 47 L88 47 M12 63 L88 63 M31 30 L31 80 M50 30 L50 80 M69 30 L69 80"/>
        <path d="M20 22 L28 6 M42 22 L50 6 M64 22 L72 6"/>
      </svg>
      <h3>Floor Preparations</h3>
      <p>Levelling and screeding so every tile sits flat and stays put.</p>
      <span class="btn-outline">Learn More</span>
    </div>
  </div>
</section>

<section class="work">
  <h2 class="section-title">View Our Work</h2>
  <div class="gallery">
    <div class="tile tile-1" role="img" aria-label="Commercial lobby with polished tiled floor"></div>
    <div class="tile tile-2">
      <h4>Sed ut perspiciatis unde omnis iste natus</h4>
      <span class="plus">+</span>
    </div>
    <div class="tile tile-3" role="img" aria-label="Glass walkway with tiled floor beside a garden"></div>
    <div class="tile tile-4" role="img" aria-label="Bright indoor space with large floor tiles"></div>
    <div class="tile tile-5" role="img" aria-label="Warm terracotta tiled room"></div>
    <div class="tile tile-6" role="img" aria-label="Outdoor paved garden path"></div>
  </div>
</section>

<section class="testimonials">
  <h2 class="section-title">Testimonials</h2>
  <div class="quotes">
    <div class="quote">
      <div class="avatar" role="img" aria-label="Client portrait"></div>
      <div>
        <p>“The team tiled our bathroom and laundry in under a week. Clean lines, no mess left behind and the waterproofing was explained clearly.”</p>
        <div class="who">Sam Reed - Tall Wave</div>
        <div class="stars">★★★★★</div>
      </div>
      <span class="qmark">”</span>
    </div>
    <div class="quote">
      <div class="avatar" role="img" aria-label="Client portrait"></div>
      <div>
        <p>“Great work on our office foyer floor. They prepared the slab properly and the stone finish still looks new a year later.”</p>
        <div class="who">Sam Reed - Tall Wave</div>
        <div class="stars">★★★★★</div>
      </div>
      <span class="qmark">”</span>
    </div>
  </div>
</section>

<footer>
  <div class="footer">
    <div class="col-links">
      <h4>Quick Link</h4>
      <ul>
        <li>Home</li><li>About Us</li><li>Services</li><li>Gallery</li><li>Ongoing Projects</li><li>Contact</li><li>News</li>
      </ul>
    </div>
    <div class="col-contact">
      <h4>Contact Us</h4>
      <div class="row">
        <svg width="12" height="16" viewBox="0 0 12 16"><path d="M6 0a6 6 0 0 0-6 6c0 4.5 6 10 6 10s6-5.5 6-10a6 6 0 0 0-6-6zm0 8.5A2.5 2.5 0 1 1 6 3.5a2.5 2.5 0 0 1 0 5z" fill="var(--green)"/></svg>
        <span>Tall Wave<br>18 Birch Lane, Northfield</span>
      </div>
      <div class="row">
        <svg width="14" height="14" viewBox="0 0 14 14"><path d="M3 0l3 3-2 2c1 2 3 4 5 5l2-2 3 3-2 3C6 14 0 8 0 3z" fill="var(--green)"/></svg>
        <span>Phone : +1 555 010 4421</span>
      </div>
      <div class="row">
        <svg width="14" height="10" viewBox="0 0 14 10"><rect width="14" height="10" fill="var(--green)"/><path d="M0 0l7 6 7-6" stroke="var(--footer)" fill="none"/></svg>
        <span>hello@tallwave.example</span>
      </div>
      <div class="social"><span></span><span></span><span></span><span></span></div>
    </div>
    <div class="col-quote">
      <h4>Get a Quote</h4>
      <p>Tell us about your project and we will reply within one working day with a clear, itemised price.</p>
      <div class="form">
        <div class="field">Name</div>
        <div class="field">Mail</div>
        <div class="field">Phone No</div>
        <a class="btn">Submit Now</a>
      </div>
    </div>
  </div>
  <div class="copyright">© 2017 Tall Wave. All Rights Reserved.</div>
</footer>

</body>
</html>
```